Copper Ridge Business Cards For New Startup

I am looking for you to design some business cards for a new startup https://copperridgehub.example. I have supplied logo, brand guidelines and our signatures as a guide.

We need this to reflect the brand guidelines and the website for brand consistency,

What is Copper Ridge?

Mallorca's Business Growth Community
Join your new business community full of passionate entrepreneurs who
love to solve problems and help each other grow together!

Any questions you can ask.

Target Market(s)

Business to Business

Contact Information for Business Card

These are attached (signatures) to the job

Font styles to use
Other font styles liked:
• Open Sans

Requirements
Must have
• Match design guidelines
Nice to have
• Photos of our faces so people remember us

```html
<!DOCTYPE html>
<html lang="en">
<head>
<meta charset="utf-8">
<title>Copper Ridge Business Cards</title>
<link href="https://fonts.googleapis.com/css2?family=Open+Sans:wght@400;600;700&display=swap" rel="stylesheet">
<style>
  :root {
    --olive: #5f6b2c;
    --olive-dark: #4d5824;
    --white: #ffffff;
    --paper: #f6f6f4;
    --backdrop: #e9e6e1;
    --photo-warm: #d9b79a;
    --photo-cool: #9aa3a8;
  }
  * { margin: 0; padding: 0; box-sizing: border-box; }
  html, body {
    width: 1200px; height: 900px; overflow: hidden;
    background: var(--backdrop);
    font-family: "Open Sans", Arial, sans-serif;
  }
  .canvas { position: relative; width: 1200px; height: 900px; }

  .card {
    position: absolute; width: 620px; height: 354px;
    box-shadow: 0 6px 18px rgba(0,0,0,.18);
  }

  /* Contact side */
  .card--contact { left: 60px; top: 80px; background: var(--white); padding: 20px; }
  .contact-panel {
    position: relative; width: 100%; height: 100%;
    background: var(--olive); color: var(--white);
    overflow: hidden;
  }
  .portrait-frame {
    position: absolute; left: 22px; top: 20px; width: 212px; height: 170px;
    background: var(--white); padding: 10px;
  }
  .portrait {
    width: 100%; height: 100%;
    background: linear-gradient(135deg, var(--photo-cool) 0%, var(--photo-warm) 55%, #efe2cf 100%);
  }
  .contact-details { position: absolute; left: 258px; top: 22px; right: 16px; }
  .person-name { font-size: 30px; font-weight: 700; line-height: 1.1; letter-spacing: .2px; white-space: nowrap; }
  .person-role { font-size: 15px; font-weight: 600; margin-top: 4px; white-space: nowrap; }
  .contact-line { font-size: 18px; font-weight: 600; margin-top: 4px; white-space: nowrap; }
  .web-box {
    position: absolute; left: 258px; right: 16px; top: 178px;
    border: 2px solid var(--white); padding: 3px 10px;
    font-size: 20px; font-weight: 600; white-space: nowrap; text-align: center;
  }
  .social-row {
    position: absolute; left: 24px; bottom: 26px;
    display: flex; gap: 14px;
  }
  .social-dot { width: 40px; height: 40px; border-radius: 50%; background: var(--white); }

  /* Brand side */
  .card--brand { left: 520px; top: 466px; background: var(--olive); padding: 24px; }
  .brand-panel {
    width: 100%; height: 100%; background: var(--paper);
    display: flex; flex-direction: column; align-items: center; justify-content: center;
    gap: 26px;
  }
  .brand-circle { width: 150px; height: 150px; border: 5px solid var(--olive); border-radius: 50%; }
  .brand-name {
    font-size: 50px; font-weight: 600; color: var(--olive);
    letter-spacing: 1px; line-height: 1; white-space: nowrap;
  }
</style>
</head>
<body>
<main class="canvas">

  <section class="card card--contact" aria-label="Business card, contact side">
    <div class="contact-panel">
      <div class="portrait-frame">
        <div class="portrait" role="img" aria-label="Portrait photo of Harriet Lindqvist"></div>
      </div>
      <div class="contact-details">
        <p class="person-name">Harriet Lindqvist</p>
        <p class="person-role">Relationship Director | Copper Ridge</p>
        <p class="contact-line">M: +44 7700 900 482</p>
        <p class="contact-line">E: hl@copperridgehub.example</p>
      </div>
      <p class="web-box">copperridgehub.example</p>
      <div class="social-row" aria-label="Social media links">
        <span class="social-dot"></span>
        <span class="social-dot"></span>
        <span class="social-dot"></span>
        <span class="social-dot"></span>
        <span class="social-dot"></span>
      </div>
    </div>
  </section>

  <section class="card card--brand" aria-label="Business card, brand side">
    <div class="brand-panel">
      <span class="brand-circle"></span>
      <p class="brand-name">COPPER RIDGE</p>
    </div>
  </section>

</main>
</body>
</html>
```